New modern business card design

To design a brand new business card that's clean & modern in terms of layout.
I have attached our company logo and also basic information regarding what is needed on the card that also needs to be editable.

Target Market(s)

motor trade

Contact Information for Business Card

logo, name, title, tel, mob, email, address, www, all information is in the word.doc file

Requirements
Must have
• white background
Nice to have
• Nice clean font

```html
<!DOCTYPE html>
<html lang="en">
<head>
<meta charset="utf-8">
<title>Bolt Works Ltd – Business Card</title>
<link rel="stylesheet" href="https://fonts.googleapis.com/css2?family=Michroma&family=Open+Sans:wght@400;600;700&display=swap">
<style>
  :root {
    --brand-blue: #1f6fb8;
    --brand-blue-light: #3f8fd2;
    --steel-grey: #9a9c9f;
    --ink: #3a3a3a;
    --card-white: #f8f8f8;
    --stage: #e6e7e9;
  }
  * { box-sizing: border-box; margin: 0; padding: 0; }
  html, body { width: 1200px; height: 950px; overflow: hidden; }
  body {
    background: var(--stage);
    font-family: "Open Sans", Arial, sans-serif;
    position: relative;
  }
  .card {
    position: absolute;
    top: 95px;
    width: 440px;
    height: 760px;
    box-shadow: 0 6px 18px rgba(0,0,0,0.18);
    overflow: hidden;
  }
  /* Front */
  .card-front { left: 130px; background: var(--card-white); }
  .edge-strip {
    position: absolute; left: 0; top: 0; bottom: 0; width: 18px;
    background: var(--brand-blue);
  }
  .edge-strip-cap {
    position: absolute; left: 0; top: 0; width: 18px; height: 150px;
    background: var(--steel-grey);
  }
  .brand {
    position: absolute; top: 95px; left: 60px; right: 40px;
    text-align: center;
  }
  .brand-name {
    font-family: "Michroma", sans-serif;
    color: var(--brand-blue);
    font-size: 33px;
    letter-spacing: 1px;
    line-height: 1.2;
  }
  .brand-rule {
    height: 2px; background: var(--brand-blue); margin: 8px 0 6px;
  }
  .brand-suffix {
    font-family: "Michroma", sans-serif;
    color: var(--steel-grey);
    font-size: 16px;
    letter-spacing: 12px;
  }
  .person { position: absolute; top: 300px; left: 60px; }
  .person-name {
    font-family: "Michroma", sans-serif;
    color: var(--brand-blue);
    font-size: 25px;
    letter-spacing: 1px;
  }
  .person-title {
    font-family: "Michroma", sans-serif;
    color: var(--steel-grey);
    font-size: 19px;
    letter-spacing: 1px;
    margin-top: 2px;
  }
  .contact-list { position: absolute; top: 395px; left: 60px; list-style: none; }
  .contact-item {
    display: flex; align-items: center; gap: 12px;
    font-weight: 700; color: var(--ink);
    font-size: 19px; line-height: 30px;
  }
  .contact-item.small { font-size: 16px; font-weight: 600; }
  .contact-icon { width: 18px; height: 18px; fill: var(--ink); flex: none; }
  .address-band {
    position: absolute; left: 0; top: 575px; width: 395px; height: 110px;
    background: linear-gradient(100deg, var(--brand-blue) 0%, var(--brand-blue-light) 55%, var(--brand-blue) 100%);
    padding: 22px 0 0 40px;
    color: #fff;
    font-family: "Michroma", sans-serif;
    font-size: 16px;
    line-height: 30px;
  }
  /* Back */
  .card-back { left: 630px; background: var(--brand-blue); }
  .back-web {
    position: absolute; left: 50px; top: 60px;
    writing-mode: vertical-rl;
    color: #fff; font-size: 16px; letter-spacing: 6px;
  }
  .back-brand {
    position: absolute; top: 50%; left: 50%;
    transform: translate(-50%, -50%);
    text-align: center;
    font-family: "Michroma", sans-serif;
    color: #fff;
    font-size: 48px;
    line-height: 1.25;
  }
</style>
</head>
<body>
  <section class="card card-front" aria-label="Business card front">
    <div class="edge-strip"></div>
    <div class="edge-strip-cap"></div>

    <header class="brand">
      <div class="brand-name">BOLT WORKS</div>
      <div class="brand-rule"></div>
      <div class="brand-suffix">LTD</div>
    </header>

    <div class="person">
      <div class="person-name">DANIEL HARTLEY</div>
      <div class="person-title">GENERAL MANAGER</div>
    </div>

    <ul class="contact-list">
      <li class="contact-item">
        <svg class="contact-icon" viewBox="0 0 24 24" aria-hidden="true"><path d="M4 7c0-2 2-3 8-3s8 1 8 3v2h-4V7H8v2H4z M6 11h12l2 9H4z M12 13a2.5 2.5 0 1 0 0 5a2.5 2.5 0 0 0 0-5z"/></svg>
        0161 496 0582
      </li>
      <li class="contact-item">
        <svg class="contact-icon" viewBox="0 0 24 24" aria-hidden="true"><path d="M7 2h10a1 1 0 0 1 1 1v18a1 1 0 0 1-1 1H7a1 1 0 0 1-1-1V3a1 1 0 0 1 1-1zm1 3v12h8V5z"/></svg>
        07700 900 418
      </li>
      <li class="contact-item small">
        <svg class="contact-icon" viewBox="0 0 24 24" aria-hidden="true"><path d="M3 6h18v12H3z M3 6l9 7 9-7" fill="none" stroke="#3a3a3a" stroke-width="2"/></svg>
        dhartley@boltworks.co.uk
      </li>
      <li class="contact-item small">
        <svg class="contact-icon" viewBox="0 0 24 24" aria-hidden="true"><circle cx="12" cy="12" r="10"/><path d="M2 12h20M12 2c3 3 3 17 0 20M12 2c-3 3-3 17 0 20" fill="none" stroke="#f8f8f8" stroke-width="1.5"/></svg>
        www.boltworks.co.uk
      </li>
    </ul>

    <address class="address-band" style="font-style:normal">
      Kestrel Road Denton<br>
      Manchester, M99 4QX
    </address>
  </section>

  <section class="card card-back" aria-label="Business card back">
    <div class="back-web">www.boltworks.co.uk</div>
    <div class="back-brand">BOLT<br>WORKS</div>
  </section>
</body>
</html>
```